IT supplier clean wordpress website - payment guaranteed

Clean website design for a wordpress based website
Design only - PSD delivery with images

current website: www.quorvel.net
please use your imagination and try something out of the box...
We like https://tavrinex.com.au as look and feel, but you don't have to copy it, you can be creative

We like the navigation header and the phone number, but do not need 'instant quote' so the 1300 phone number and the 'lock' icon for login can be on the same line

Site Map:
IT support
VoIP
Internet and Data
Cloud hosting
About
Contact

Our logo is attached, it can be used light or dark.
Our only color used is the warm grey Pantone 8003C hex #877A69

You will only need to design the homepage to win the competition, but the winning designer will be required to supply without extra charges:
1. Home page design
2. A second, standard page template design
3. An icon set in colors appropriate to the site that have icons to match the subjects in these pages:
https://tavrinex.com.au/products/
https://tavrinex.com.au/making-the-switch/
https://tavrinex.com.au/why-tavrinex/
We will create a single page version of the options on https://tavrinex.com.au/solutions/
4.Any images used

Please avoid stock photos that are too common - e.g. smiling woman with headset, try to make the design stand out with simple images and well-designed layout.

Target Market(s)

Mid-size business clients

Industry/Entity Type

It Company

Number of Pages Required

1 page

Requirements
Must have
• Quor logo
• Use Quor color

```html
<!DOCTYPE html>
<html lang="en">
<head>
<meta charset="utf-8">
<title>Quor — IT Outsourcing</title>
<link href="https://fonts.googleapis.com/css2?family=Cousine:wght@400;700&family=Open+Sans:wght@400;600&display=swap" rel="stylesheet">
<style>
:root{
  --warm-grey:#877A69;
  --ink:#1d1d22;
  --night:#34323f;
  --orange:#ff6a1a;
  --orange-light:#ff8a3c;
  --sky:#4a9df0;
  --line:#dcdce4;
  --mist:#f5f5fb;
  --mist-border:#cfe3f5;
  --text-grey:#9a9a9a;
  --white:#ffffff;
}
*{margin:0;padding:0;box-sizing:border-box}
html,body{width:1200px;height:2586px;overflow:hidden}
body{position:relative;background:var(--white);font-family:"Cousine",monospace;color:var(--ink)}
.abs{position:absolute}
h1,h2,h3{font-weight:400}

/* hero */
.hero{left:0;top:0;width:1200px;height:597px;background:
  radial-gradient(ellipse at 70% 35%,#8a8178 0%,rgba(138,129,120,0) 55%),
  linear-gradient(180deg,#a08f7d 0%,#8c7561 45%,#b08a68 70%,#9a8472 100%)}
.hero-shade{left:0;top:0;width:1200px;height:597px;background:rgba(90,78,64,.25)}
.site-header{left:0;top:0;width:1200px;height:93px;background:rgba(135,122,105,.88)}
.brand-name{left:190px;top:22px;font-family:"Cousine",monospace;font-size:34px;color:var(--white)}
.phone{left:800px;top:15px;font-family:"Open Sans",sans-serif;font-size:13px;color:var(--white);display:flex;align-items:center;gap:6px}
.login{left:937px;top:14px;width:68px;height:22px;background:var(--orange);color:var(--white);font-family:"Open Sans",sans-serif;font-size:10px;text-align:center;line-height:22px;border-radius:2px}
.nav{top:70px;font-family:"Open Sans",sans-serif;font-size:14px;color:var(--white)}
.nav.active{color:var(--orange)}
.nav.active::after{content:"";position:absolute;left:0;right:0;bottom:-3px;height:1px;background:var(--orange)}
.hero-title{left:196px;top:224px;font-size:54px;line-height:76px;color:var(--white);letter-spacing:2px}
.signup{left:193px;top:484px;width:159px;height:45px;background:linear-gradient(180deg,var(--orange-light),var(--orange));color:var(--white);font-family:"Open Sans",sans-serif;font-size:22px;text-align:center;line-height:45px;border-radius:2px}

/* right people */
.people{left:0;top:597px;width:1200px;height:216px;background:var(--night)}
.section-title{left:0;width:1200px;text-align:center;font-size:25px}
.people .section-title{top:34px;color:var(--white)}
.people-copy{left:218px;top:88px;width:764px;text-align:center;font-size:12px;line-height:24px;color:#8d8c95}
.people-copy u{text-decoration:none;border-bottom:1px solid #8d8c95}

/* services */
.services-title{top:840px}
.service-link{left:271px;top:1018px;width:658px;height:2px;background:var(--line)}
.service{width:172px;height:172px;border:2px solid var(--line);border-radius:50%;background:var(--white);top:932px;display:flex;align-items:center;justify-content:center}
.service-label{top:1118px;width:300px;text-align:center;font-size:16px}

/* products */
.products{left:0;top:1197px;width:1200px;height:648px;background:var(--mist);border:2px solid var(--mist-border)}
.products-title{top:1220px}
.timeline{left:204px;top:1318px;width:3px;height:472px;background:#c9c9d6}
.dot{width:18px;height:18px;border:3px solid var(--sky);border-radius:50%;background:var(--white);left:196px}
.product-name{left:389px;font-size:24px;color:var(--warm-grey)}
.product-copy{left:389px;width:500px;font-size:13px;line-height:19px;color:var(--text-grey)}
.product-link{font-size:12px;color:#6e6e6e}
.see-more{left:529px;top:1800px;width:146px;height:32px;border:3px solid #b8d7f2;background:var(--white);font-size:12px;text-align:center;line-height:26px;color:#555}

/* partners */
.partners-title{top:1902px}
.badge{top:2004px;width:92px;height:92px;border-radius:6px}
.badge.solid{background:#26596d}
.badge.soft{background:#e6e6e6;border-radius:50%;width:60px;height:60px;top:2000px}
.badge.card{background:linear-gradient(180deg,#f2f2f2,#d5d5d5);border:1px solid #c7c7c7;width:128px;height:96px}

/* call to action */
.cta{left:0;top:2158px;width:1200px;height:150px;background:#f3f3f8}
.cta-copy{left:0;top:2194px;width:1200px;text-align:center;font-size:20px;line-height:35px;color:var(--warm-grey)}
.cta-copy span{color:var(--ink);border-bottom:1px solid var(--ink)}

/* footer */
.footer{left:0;top:2308px;width:1200px;height:235px;background:var(--warm-grey)}
.footer-head{top:2346px;font-size:14px;color:var(--white)}
.footer-text{font-size:10.5px;line-height:16px;color:#efe9e1}
.footer-rule{top:2346px;width:1px;height:158px;background:rgba(255,255,255,.25)}
.footer-name{left:820px;top:2400px;font-family:"Cousine",monospace;font-size:56px;color:rgba(255,255,255,.4)}
.legal{left:0;top:2543px;width:1200px;height:43px;background:var(--night);text-align:center;line-height:43px;font-size:10px;color:#cfcfd6}
</style>
</head>
<body>

<div class="abs hero" role="img" aria-label="Photo of an open laptop on a wooden desk with a soft blurred background"></div>
<div class="abs hero-shade"></div>

<header class="abs site-header"></header>
<div class="abs brand-name">Quor</div>
<div class="abs phone">
  <svg width="15" height="15" viewBox="0 0 24 24" fill="none" stroke="#ff8a3c" stroke-width="2"><path d="M5 3h4l2 5-3 2a11 11 0 0 0 6 6l2-3 5 2v4a2 2 0 0 1-2 2A17 17 0 0 1 3 5a2 2 0 0 1 2-2z"/></svg>
  090.000.4521
</div>
<div class="abs login">Login</div>
<nav>
  <div class="abs nav active" style="left:545px">Home</div>
  <div class="abs nav" style="left:616px">Services</div>
  <div class="abs nav" style="left:695px">Products</div>
  <div class="abs nav" style="left:782px">Malware</div>
  <div class="abs nav" style="left:870px">About us</div>
  <div class="abs nav" style="left:957px">Contact</div>
</nav>

<h1 class="abs hero-title">IT OUTSOURCING<br>THE WAY IT<br>SHOULD BE</h1>
<div class="abs signup">Sign Up</div>

<section class="abs people">
  <h2 class="abs section-title">The Right People</h2>
  <p class="abs people-copy">Not only does Quor have highly <u>qualified people</u>, with certifications from Veltrix, Norvane, National <u>Comms Board</u> amongst others, but importantly we can speak plain English and translate IT questions into a language you can understand and make <u>decisions easier</u> for you.</p>
</section>

<h2 class="abs section-title services-title">Our Services</h2>
<div class="abs service-link"></div>
<div class="abs service" style="left:185px">
  <svg width="90" height="90" viewBox="0 0 90 90" fill="none" stroke="var(--sky)" stroke-width="5" stroke-linecap="round">
    <path d="M18 50V42a27 27 0 0 1 54 0v8"/>
    <rect x="14" y="44" width="12" height="24" rx="5" fill="var(--sky)"/>
    <rect x="64" y="44" width="12" height="24" rx="5" fill="var(--sky)"/>
    <path d="M70 68c0 8-8 12-18 12"/>
    <rect x="38" y="76" width="16" height="8" rx="4" fill="var(--sky)"/>
  </svg>
</div>
<div class="abs service-label" style="left:121px">Data And Voice</div>
<div class="abs service" style="left:514px">
  <svg width="120" height="90" viewBox="0 0 120 90">
    <path d="M30 76a22 22 0 0 1 2-44 30 30 0 0 1 56 6 19 19 0 0 1 2 38z" fill="var(--sky)"/>
    <path d="M60 66V38M48 50l12-12 12 12" fill="none" stroke="var(--white)" stroke-width="7" stroke-linecap="round" stroke-linejoin="round"/>
  </svg>
</div>
<div class="abs service-label" style="left:450px">Cloud Services</div>
<div class="abs service" style="left:843px">
  <div role="img" aria-label="Support agent illustration" style="width:92px;height:92px;border-radius:50%;background:#dbeafb"></div>
</div>
<div class="abs service-label" style="left:779px">Support</div>

<section class="abs products"></section>
<h2 class="abs section-title products-title">Our Products</h2>
<div class="abs timeline"></div>
<div class="abs dot" style="top:1309px"></div>
<div class="abs dot" style="top:1577px"></div>

<svg class="abs" style="left:232px;top:1312px" width="90" height="80" viewBox="0 0 90 80" fill="none" stroke="var(--sky)" stroke-width="3">
  <rect x="4" y="4" width="22" height="70" rx="2"/>
  <line x1="9" y1="16" x2="21" y2="16"/><line x1="9" y1="24" x2="21" y2="24"/>
  <rect x="32" y="8" width="52" height="40" rx="2"/>
  <rect x="38" y="14" width="40" height="28"/>
  <path d="M52 48v12M64 48v12M42 62h32"/>
</svg>
<h3 class="abs product-name" style="top:1305px">Corporate Workstations</h3>
<p class="abs product-copy" style="top:1350px">Robust, business grade performance and reliability. Why choose any other PC when you can afford Kestrel.</p>
<div class="abs product-link" style="left:389px;top:1420px">Read More</div>
<div class="abs product-link" style="left:505px;top:1420px">View Product</div>

<svg class="abs" style="left:224px;top:1562px" width="100" height="70" viewBox="0 0 100 70" fill="none" stroke="var(--sky)" stroke-width="3">
  <rect x="22" y="4" width="56" height="34" rx="2"/>
  <rect x="4" y="22" width="36" height="26" rx="2" fill="var(--mist)"/>
  <rect x="60" y="22" width="36" height="26" rx="2" fill="var(--mist)"/>
  <path d="M22 48v8M14 58h16M78 48v8M70 58h16"/>
  <path d="M40 34h20"/>
</svg>
<h3 class="abs product-name" style="top:1561px">Luma Desk, Book, Pad and Phone</h3>
<p class="abs product-copy" style="top:1604px">Great for home and the kids. Sleek, stylish and capable. You can easily integrate with your business systems if you have the Quor advantage. Use Luma Pads and Luma Phone with RDP, Mailhub and custom apps.</p>
<div class="abs product-link" style="left:389px;top:1720px">Read More</div>
<div class="abs product-link" style="left:505px;top:1720px">View Product</div>
<div class="abs see-more">See More</div>

<h2 class="abs section-title partners-title">We’ve Worked With</h2>
<div class="abs badge solid" style="left:195px"></div>
<div class="abs badge soft" style="left:390px"></div>
<div class="abs badge card" style="left:533px"></div>
<div class="abs badge solid" style="left:727px"></div>
<div class="abs badge soft" style="left:920px"></div>

<section class="abs cta"></section>
<p class="abs cta-copy">We’re taking new projects, and growing our team.<br>Drop us a line:<span>info@quor.net</span></p>

<footer class="abs footer"></footer>
<div class="abs footer-head" style="left:204px">Contact Info</div>
<div class="abs footer-text" style="left:186px;top:2374px">
  <div style="display:flex;gap:6px;align-items:center"><svg width="14" height="14" viewBox="0 0 24 24" fill="none" stroke="#fff" stroke-width="2"><path d="M5 3h4l2 5-3 2a11 11 0 0 0 6 6l2-3 5 2v4a2 2 0 0 1-2 2A17 17 0 0 1 3 5a2 2 0 0 1 2-2z"/></svg>+61 (2) 80405517</div>
  <div style="display:flex;gap:6px;align-items:center;margin-top:8px"><svg width="14" height="14" viewBox="0 0 24 24" fill="none" stroke="#fff" stroke-width="2"><rect x="3" y="5" width="18" height="14"/><path d="M3 6l9 7 9-7"/></svg>+61 (2) 80405518</div>
  <div style="display:flex;gap:6px;align-items:flex-start;margin-top:8px"><svg width="14" height="16" viewBox="0 0 24 28" fill="none" stroke="#fff" stroke-width="2"><path d="M12 26s9-9 9-15a9 9 0 0 0-18 0c0 6 9 15 9 15z"/><circle cx="12" cy="11" r="3"/></svg><span>Suite 7, 14-18 Larkin<br>St,Redfern NSW<br>2016</span></div>
</div>
<div class="abs footer-rule" style="left:378px"></div>
<div class="abs footer-head" style="left:395px">Company</div>
<div class="abs footer-text" style="left:395px;top:2372px">IT support<br>VoIP<br>Internet<br>and Data<br>Cloud<br>hosting<br>About<br>Contact</div>
<div class="abs footer-rule" style="left:510px"></div>
<div class="abs footer-head" style="left:563px">Company</div>
<div class="abs footer-text" style="left:563px;top:2372px">Privacy Policy<br>Terms &amp; Conditions</div>
<div class="abs footer-name">Quor</div>

<div class="abs legal">© 2017 Quor. All rights reserved.</div>
</body>
</html>
```